Broschüre für Beratung, Planung, und Serviceerbringung für Bauprojekte von industriellen und öffentlichen Auftraggebern
Zielgruppe
Die KDR | Group ist eine mittelständige und überregional tätige Unternehmensgruppe, deren Schwerpunkt die Beratung, Planung, und Serviceerbringung für Bauprojekte von industriellen und öffentlichen Auftraggebern ist.
KDR ist seit mehr als 30 Jahren ein kompetenter Ansprechpartner für alle Bereiche der Bautechnik sowie damit zusammenhängenden Fachplanungen und begleitet mit seinen mehr als 50 festangestellten Mitarbeitern die Kunden vom Projektstart über die Planungs-, die Projektvorbereitungs- und Bauphase bis zum „Einzug“ bzw. zur Inbetriebnahme.
Ziel der KDR | Group ist es, gemeinsam mit dem Kunden einen reibungslosen und erfolgreichen Projektablauf sicherzustellen und abzuschließen.
Mit den Anforderungen der Kunden hat sich KDR zu einem überregional tätigen Ingenieur- und Servicedienstleister entwickelt, dessen Geschäftsführung, Verwaltung einschl. IT- Development & Support, in Falkenried ansässig ist.
Am Standort Falkenried befindet sich auch ein technischer Bürostandort, der schwerpunktmäßig Projekte im Kreis Haselbrunn-Eichtal bearbeitet aber auch eng mit den weiteren Bürostandorten in Kornstedt, Sommerfeld an der Lohe-Brückau, Tellborn und Marienquell vernetzt ist und zusammenarbeitet.
Aufgabenstellung
Eine moderne Firmenbroschüre, Bilder sind einige vorhanden

```html
<!DOCTYPE html>
<html lang="de">
<head>
<meta charset="utf-8">
<title>Projektreferenzen</title>
<link rel="stylesheet" href="https://fonts.googleapis.com/css2?family=Montserrat:wght@800&family=Raleway:wght@400;500&display=swap">
<style>
  :root {
    --backdrop: #e4e4e4;
    --paper: #fbfbfb;
    --taupe: #7b716a;
    --band-light: #c3bfbb;
    --text: #3b3835;
    --bullet: #55504c;
  }
  * { box-sizing: border-box; margin: 0; padding: 0; }
  html, body { width: 1200px; height: 952px; overflow: hidden; }
  body {
    background: var(--backdrop);
    font-family: "Raleway", sans-serif;
    color: var(--text);
    position: relative;
  }
  .spread {
    position: absolute;
    left: 20px; top: 66px;
    width: 1160px; height: 820px;
    display: flex;
    box-shadow: 0 10px 30px rgba(0,0,0,.18);
  }
  .page {
    position: relative;
    width: 580px; height: 820px;
    background: var(--paper);
    overflow: hidden;
  }
  .page--left { background: linear-gradient(90deg, #fbfbfb 85%, #eeeeee 100%); }
  .page--right { background: linear-gradient(90deg, #ececec 0%, #fbfbfb 12%); }
  .page__header { position: absolute; left: 0; top: 0; width: 580px; height: 340px; display: block; }
  .page__number {
    position: absolute; bottom: 22px;
    font-size: 8px; color: var(--text);
  }
  .page--left .page__number { right: 26px; }
  .page--right .page__number { right: 22px; }
  .section-title {
    position: absolute; left: 46px; top: 352px;
    font-family: "Montserrat", sans-serif;
    font-weight: 800; font-size: 18.5px; letter-spacing: .04em;
    color: var(--taupe); text-transform: uppercase; white-space: nowrap;
  }
  .reference-list {
    position: absolute;
    list-style: none;
    font-size: 10.6px; line-height: 1.32; font-weight: 500;
  }
  .reference-list li { position: relative; padding-left: 16px; margin-bottom: 2px; }
  .reference-list li::before {
    content: ""; position: absolute; left: 0; top: 5px;
    width: 5px; height: 5px; border-radius: 50%; background: var(--bullet);
  }
  .reference-list--left { left: 48px; top: 392px; width: 400px; }
  .reference-list--col1 { left: 40px; top: 350px; width: 250px; }
  .reference-list--col2 { left: 312px; top: 350px; width: 245px; }
</style>
</head>
<body>
<main class="spread">
  <section class="page page--left">
    <svg class="page__header" viewBox="0 0 580 340">
      <defs>
        <linearGradient id="siteGradient" x1="0" y1="0" x2="1" y2="1">
          <stop offset="0" stop-color="#5a5348"/>
          <stop offset=".45" stop-color="#c9a15a"/>
          <stop offset=".7" stop-color="#f3d9a8"/>
          <stop offset="1" stop-color="#7fa9c9"/>
        </linearGradient>
      </defs>
      <path d="M0 0 H580 V265 C420 250 220 255 0 262 Z" fill="url(#siteGradient)" role="img" aria-label="Foto: Rohbau mit Bagger und Kran im Gegenlicht"/>
      <path d="M0 262 C220 255 420 250 580 265 V300 C430 275 240 268 0 292 Z" fill="var(--band-light)"/>
      <path d="M0 292 C240 268 430 275 580 300 V308 C430 290 220 290 0 330 Z" fill="var(--taupe)"/>
    </svg>
    <h1 class="section-title">Ein Auszug unserer Projektreferenzen</h1>
    <ul class="reference-list reference-list--left">
      <li>Neu- und Umbau sowie Sanierung von Produktions-, Fertigungs- und Verwaltungsgebäuden</li>
      <li>Sanierung von Auffangtassen gemäß WHG</li>
      <li>Neubau, Sanierung und Erweiterungen von Abfüllflächen (VAwS)</li>
      <li>Durchführung von VAwS-Maßnahmen in Produktions- und Fertigungsbereichen</li>
      <li>Erstellung von Brandschutzkonzepten</li>
      <li>Umsetzung von Brandschutzauflagen und Brandschutzkonzepten sowie baubegleitende Beratungen und Überwachung</li>
      <li>Modifizierung der Löschwasserrückhaltung von Produktions- und Fertigungsgebäuden</li>
      <li>Errichtung von Siloanlagen</li>
      <li>Abriss von Produktionsgebäuden einschl. Anlagenreinigung und Anlagenrückbau</li>
      <li>Asbestbewertung und Asbestsanierungen</li>
      <li>Korrosionsschutzarbeiten innerhalb von Produktionsstätten</li>
      <li>Betonsanierungsarbeiten</li>
      <li>Neubau und Erneuerung von Versorgungsleitungen</li>
      <li>Neubau und Sanierung von Brückenbauwerken</li>
      <li>Neubau und Sanierung von Abwasserkanalnetzen einschl. den dazugehörigen Absperr- und Sicherheitseinrichtungen für die Löschwasserrückhaltung</li>
      <li>Neubau, Erweiterung sowie Sanierung von Straßen, Wegen und Plätzen</li>
    </ul>
    <span class="page__number">5</span>
  </section>

  <section class="page page--right">
    <svg class="page__header" viewBox="0 0 580 340">
      <defs>
        <linearGradient id="buildingGradient" x1="0" y1="0" x2="0" y2="1">
          <stop offset="0" stop-color="#e6e3df"/>
          <stop offset=".6" stop-color="#d9d8d6"/>
          <stop offset="1" stop-color="#5f5e5c"/>
        </linearGradient>
      </defs>
      <path d="M0 0 H580 V240 C400 250 200 270 0 290 Z" fill="url(#buildingGradient)" role="img" aria-label="Foto: weißes Produktions- und Verwaltungsgebäude mit Lieferwagen"/>
      <path d="M0 290 C200 270 400 250 580 240 V258 C400 262 200 285 0 310 Z" fill="var(--band-light)"/>
      <path d="M0 290 C120 278 180 272 240 268 C150 280 60 300 0 330 Z" fill="var(--taupe)"/>
    </svg>
    <ul class="reference-list reference-list--col1">
      <li>Neubau von Kaltwasser- und Kühlwasserrückkühlanlagen</li>
      <li>Modifizierung von VT-Anlagen und deren Komponenten</li>
      <li>Herstellung von Maschinen- und Anlagenfundamenten innerhalb vorhandener Fertigungs- und Produktionsstätten</li>
      <li>Einbau von Trafostationen in Produktionsgebäude</li>
      <li>Kaminerhöhungen von Triebwerksprüfständen</li>
      <li>Sanierung einer Galvanik sowie der dazugehörigen Wasseraufbereitungsanlage</li>
      <li>Einbau von Lagerpaternoster in Produktionsbereiche</li>
      <li>Neu- und Umbau von Röntgenräumen</li>
      <li>Aufstell- und Komponentenplanung im Zuge der Erneuerung einer gesamten Produktionsstätte</li>
      <li>Neuinstallation von Be- und Entlüftungs- sowie Klimatisierungsanlagen in bestehende Produktions- und Fertigungsgebäude</li>
      <li>Installation von Rauch- und Wärmeabzugsanlagen in bestehende Produktions- und Fertigungsgebäude</li>
      <li>Umsetzung von Brandschutzmaßnahmen bei der Fassadensanierungsarbeiten an Produktions- und Verwaltungsgebäuden in Zusammenarbeit mit der Denkmalschutzbehörde</li>
    </ul>
    <ul class="reference-list reference-list--col2">
      <li>Projektsteuerung für den baulichen Bereich eines Produktionsbereiches einschl. Schnittstellenmanagement zum Anlagenbau und der technischen Gebäudeausrüstung</li>
      <li>Baukoordination im Zuge von Hoch- und Tiefbauarbeiten bei Neu- und Umbau sowie Sanierungsmaßnahmen</li>
      <li>Ganzheitliche Beratungen für den baulichen Brandschutz</li>
      <li>Erstellung von schutzzielorientierten Brandschutzkonzepten</li>
      <li>Sachverständigenwesen für den baulichen Brandschutz</li>
      <li>Bauzustandsanalyse und Schadensbewertung</li>
      <li>Instandsetzungs- und Instandhaltungsplanung</li>
      <li>Beratende und projektbegleitende Ingenieurleistungen als Sachkundiger gemäß TRGS 519, Anlage 3 für Abbruch-, Sanierungs- und Instandhaltungsarbeiten an asbesthaltigen Gefahrstoffen einschließlich Asbestzementprodukten nach Gefahrstoffverordnung Anhang III, Ziff. 2.4.2 Abs. 3</li>
    </ul>
    <span class="page__number">6</span>
  </section>
</main>
</body>
</html>
```